Business Cards

I'd like help creating business cards with the full logo "Veltrona Capital Partners" on the back of the card (navy background with white writing), and abbreviated logo "VCP" on the front. Would like to list name, title, phone number, email, and website listed on front of card. Would like to keep very simple. Front font Arial or similar.

```html
<!DOCTYPE html>
<html lang="en">
<head>
<meta charset="utf-8">
<title>Veltrona Capital Partners – Business Card</title>
<link rel="stylesheet" href="https://fonts.googleapis.com/css2?family=Montserrat:wght@600&family=Ubuntu:wght@400;500;700&display=swap">
<style>
  :root {
    --page-bg: #ffffff;
    --card-white: #ffffff;
    --ink: #111111;
    --navy: #1f3769;
    --on-navy: #ffffff;
    --card-shadow: rgba(0, 0, 0, 0.18);
  }
  * { margin: 0; padding: 0; box-sizing: border-box; }
  html, body {
    width: 1200px;
    height: 1200px;
    overflow: hidden;
    background: var(--page-bg);
  }
  .canvas {
    position: relative;
    width: 1200px;
    height: 1200px;
  }
  .card {
    position: absolute;
    left: 165px;
    width: 871px;
    height: 510px;
    box-shadow: 0 1px 4px var(--card-shadow);
  }
  .card--front { top: 66px; background: var(--card-white); color: var(--ink); font-family: "Ubuntu", Arial, sans-serif; }
  .card--back  { top: 626px; background: var(--navy); color: var(--on-navy); font-family: "Montserrat", Arial, sans-serif; }

  /* Front */
  .front-wordmark {
    position: absolute;
    left: 62px;
    top: 70px;
    font-family: "Ubuntu", Arial, sans-serif;
    font-weight: 500;
    font-size: 112px;
    line-height: 1;
    letter-spacing: 2px;
    color: var(--ink);
  }
  .corner-bracket {
    position: absolute;
    left: 660px;
    top: 69px;
    width: 161px;
    height: 389px;
  }
  .corner-bracket line { stroke: var(--ink); stroke-width: 11; }

  .contact-list {
    position: absolute;
    left: 58px;
    top: 330px;
    list-style: none;
  }
  .contact-list li {
    display: flex;
    align-items: center;
    height: 33.5px;
    font-size: 20px;
    font-weight: 400;
  }
  .contact-icon {
    width: 14px;
    height: 14px;
    margin-right: 14px;
    fill: var(--ink);
  }

  .holder {
    position: absolute;
    right: 103px;
    top: 345px;
    text-align: right;
  }
  .holder-name {
    font-size: 30px;
    font-weight: 700;
    line-height: 1.2;
  }
  .holder-title {
    font-size: 20px;
    font-weight: 400;
    line-height: 1.3;
  }

  /* Back */
  .back-brand {
    position: absolute;
    left: 0;
    right: 0;
    top: 170px;
    text-align: center;
    font-weight: 600;
    line-height: 1;
  }
  .back-brand-name {
    display: block;
    font-size: 92px;
    letter-spacing: 4px;
  }
  .back-brand-sub {
    display: block;
    margin-top: 26px;
    font-size: 34px;
    letter-spacing: 9px;
  }
</style>
</head>
<body>
<main class="canvas">

  <section class="card card--front" aria-label="Business card front">
    <div class="front-wordmark">VCP</div>

    <svg class="corner-bracket" viewBox="0 0 161 389" aria-hidden="true">
      <line x1="0" y1="5.5" x2="161" y2="5.5"/>
      <line x1="155.5" y1="0" x2="155.5" y2="389"/>
      <line x1="50" y1="383.5" x2="161" y2="383.5"/>
    </svg>

    <ul class="contact-list">
      <li>
        <svg class="contact-icon" viewBox="0 0 14 14" aria-hidden="true"><path d="M3 1l2.2 2.6-1.3 1.6c.8 1.8 2.1 3.1 3.9 3.9l1.6-1.3L12 10l-1.1 2.4C6 12.4 1.6 8 1.6 3.1z"/></svg>
        <span class="contact-text">800-555-0142</span>
      </li>
      <li>
        <svg class="contact-icon" viewBox="0 0 14 14" aria-hidden="true"><rect x="3.5" y="1" width="7" height="3.5"/><rect x="1" y="5" width="12" height="5.5" rx="1"/><rect x="3.5" y="9" width="7" height="4" fill="#fff" stroke="#111" stroke-width="1.2"/></svg>
        <span class="contact-text">422-555-0190</span>
      </li>
      <li>
        <svg class="contact-icon" viewBox="0 0 14 14" aria-hidden="true"><rect x="1" y="3" width="12" height="8.5" rx="1"/><path d="M1.5 3.5L7 7.5l5.5-4" fill="none" stroke="#fff" stroke-width="1.2"/></svg>
        <span class="contact-text">info@vcp.com</span>
      </li>
      <li>
        <svg class="contact-icon" viewBox="0 0 14 14" aria-hidden="true"><circle cx="7" cy="7" r="6" fill="none" stroke="#111" stroke-width="1.4"/><ellipse cx="7" cy="7" rx="2.6" ry="6" fill="none" stroke="#111" stroke-width="1.2"/><line x1="1" y1="7" x2="13" y2="7" stroke="#111" stroke-width="1.2"/></svg>
        <span class="contact-text">VCP.com</span>
      </li>
    </ul>

    <div class="holder">
      <p class="holder-name">Dorian K Halvorsen III</p>
      <p class="holder-title">Attorney at Law</p>
    </div>
  </section>

  <section class="card card--back" aria-label="Business card back">
    <h1 class="back-brand">
      <span class="back-brand-name">VELTRONA</span>
      <span class="back-brand-sub">CAPITAL PARTNERS</span>
    </h1>
  </section>

</main>
</body>
</html>
```